Thornbecks Winery label master

We are looking for a classic and vintage looking wine label. Focus is on updating the family coat of arms with both color and without color. Font to be legible but classic in nature. For the label we need be able to change out the varietal and vintage and location/AVA but for the first design project we would like to use the year/vintage 2016 and the varietal/type of wine : Pinot Noir and for the AVA it will say Central Coast.

Target Market(s)

Wine drinkers between ages 30-70

Industry/Entity Type

Winery

Logo Text

Thornbeck

Font styles to use
Script

Requirements
Must have
• Thornbeck Coat of Arms with vines on top and the motto. Label size must not be over 5.5 x 3"
Nice to have
• Classic natural color and off black color fonts
Should not have
• Anything eligible or hard to read. Classic and Elegant but not overly ornate

```html
<!DOCTYPE html>
<html lang="en">
<head>
<meta charset="utf-8">
<title>Thornbeck Pinot Noir – Label</title>
<link rel="stylesheet" href="https://fonts.googleapis.com/css2?family=Lobster&family=Playfair+Display:ital,wght@1,400&family=Alfa+Slab+One&display=swap">
<style>
  :root {
    --paper: #ffffff;
    --ink: #0b0b0b;
    --gold: #c9a14a;
    --ornament-light: #4a4a4a;
    --ornament-dark: #2c2c2c;
  }
  html, body {
    margin: 0;
    padding: 0;
    width: 1200px;
    height: 1100px;
    overflow: hidden;
    background: var(--paper);
  }
  .label-canvas {
    display: block;
    width: 1200px;
    height: 1100px;
  }
  .shield-outer { fill: var(--ink); }
  .shield-band { fill: var(--paper); }
  .shield-field { fill: var(--ink); }
  .shield-rule { fill: none; stroke: var(--gold); stroke-width: 3; }
  .ornament { fill: url(#ornamentTone); }
  .ornament-rule { fill: none; stroke: var(--paper); stroke-width: 2.5; stroke-linecap: round; }
  .brand-name {
    font-family: 'Lobster', cursive;
    font-size: 82px;
    fill: var(--paper);
  }
  .varietal-banner { fill: var(--paper); stroke: var(--gold); stroke-width: 3; }
  .varietal-name {
    font-family: 'Playfair Display', serif;
    font-style: italic;
    font-size: 31px;
    letter-spacing: 3.5px;
    fill: var(--ink);
  }
  .region-name {
    font-family: 'Playfair Display', serif;
    font-style: italic;
    font-size: 31px;
    letter-spacing: 4.5px;
    fill: var(--paper);
  }
  .quality-mark {
    font-family: 'Alfa Slab One', serif;
    font-size: 27px;
    letter-spacing: 3.5px;
    fill: var(--paper);
  }
</style>
</head>
<body>
<svg class="label-canvas" viewBox="0 0 1200 1100" xmlns="http://www.w3.org/2000/svg">
  <defs>
    <path id="shield" d="M 360 295 C 450 282, 520 222, 600 222 C 680 222, 750 282, 840 295 A 24 24 0 0 0 864 320 C 900 360, 902 420, 896 470 C 888 560, 868 680, 864 782 A 24 24 0 0 0 840 808 C 760 820, 680 880, 600 880 C 520 880, 440 820, 360 808 A 24 24 0 0 0 336 782 C 332 680, 312 560, 304 470 C 298 420, 300 360, 336 320 A 24 24 0 0 0 360 295 Z"/>
    <radialGradient id="ornamentTone" cx="50%" cy="50%" r="60%">
      <stop offset="0" stop-color="var(--ornament-light)"/>
      <stop offset="1" stop-color="var(--ornament-dark)"/>
    </radialGradient>
  </defs>

  <g class="shield">
    <use href="#shield" class="shield-outer"/>
    <use href="#shield" class="shield-band" transform="translate(600 550) scale(0.975) translate(-600 -550)"/>
    <use href="#shield" class="shield-field" transform="translate(600 550) scale(0.955) translate(-600 -550)"/>
    <use href="#shield" class="shield-rule" transform="translate(600 550) scale(0.935) translate(-600 -550)"/>
  </g>

  <g class="ornament-top">
    <path class="ornament-rule" d="M 388 372 Q 430 368 478 352"/>
    <path class="ornament-rule" d="M 812 372 Q 770 368 722 352"/>
    <ellipse class="ornament" role="img" aria-label="Ornamental scrollwork flourish" cx="600" cy="325" rx="125" ry="33"/>
  </g>

  <text class="brand-name" x="600" y="485" text-anchor="middle">Thornbeck</text>

  <g class="varietal">
    <path class="varietal-banner" d="M 449 520 Q 600 508 751 520 Q 744 545 751 570 Q 600 560 449 570 Q 456 545 449 520 Z"/>
    <text class="varietal-name" x="600" y="550" text-anchor="middle">Pinot Noir</text>
  </g>

  <text class="region-name" x="600" y="613" text-anchor="middle">Central Coast</text>

  <text class="quality-mark" x="600" y="677" text-anchor="middle">PREMIUM</text>
  <text class="quality-mark" x="600" y="719" text-anchor="middle">QUALITY</text>

  <g class="ornament-bottom">
    <path class="ornament-rule" d="M 414 764 L 492 762"/>
    <path class="ornament-rule" d="M 786 764 L 708 762"/>
    <ellipse class="ornament" role="img" aria-label="Ornamental scrollwork flourish" cx="600" cy="780" rx="105" ry="26"/>
  </g>
</svg>
</body>
</html>
```